R T Security Flyer - Security Based Company

Security company offering installation of CCTV and Intruder alarm systems mainly but not limited to home alarms. Feel free to be creative

Target Market(s)

Residential and Commercial properties, Facility Managers, local business

Requirements
Must have
• smart professional finish, logo and latest up to date pictures if on kit

```html
<!DOCTYPE html>
<html lang="en">
<head>
<meta charset="utf-8">
<title>R T Security – Flyer</title>
<link href="https://fonts.googleapis.com/css2?family=Open+Sans:ital,wght@0,400;0,600;0,700;1,400;1,600&display=swap" rel="stylesheet">
<style>
  :root{
    --orange:#e8491d;
    --ink:#1b1b1b;
    --ink-soft:#2a2a2a;
    --paper:#ffffff;
    --text-dark:#333333;
    --text-light:#e6e6e6;
  }
  *{box-sizing:border-box;margin:0;padding:0}
  html,body{width:1200px;height:3600px;overflow:hidden}
  body{
    background:linear-gradient(180deg,#a8a8a8 0%,#8e8e8e 100%);
    font-family:"Open Sans",Arial,sans-serif;
    position:relative;
  }
  .page{
    position:absolute;left:80px;width:1040px;height:1471px;
    background:var(--paper);overflow:hidden;
    box-shadow:0 10px 30px rgba(0,0,0,.35);
  }
  .page--front{top:220px}
  .page--back{top:1871px}
  .abs{position:absolute}
  .photo{position:absolute}

  /* ---------- brand block ---------- */
  .brand-box{background:var(--ink);display:flex;align-items:center;justify-content:center;gap:14px}
  .brand-square{width:18px;height:18px;background:var(--text-light);flex:0 0 18px}
  .brand-name{color:var(--text-light);font-weight:600;font-size:28px;white-space:nowrap}

  /* ---------- front ---------- */
  .hero-photo{left:0;top:0;width:1040px;height:1000px;
    background:linear-gradient(160deg,#f1efec 0%,#d9d6d1 35%,#8c8a86 62%,#3b3a38 100%)}
  .hero-decor{left:0;top:0;width:1040px;height:1000px}
  .brand-box--front{left:53px;top:0;width:281px;height:360px}
  .headline-box{left:430px;top:592px;width:610px;height:254px;background:var(--orange);
    clip-path:polygon(9% 0,100% 0,100% 74%,94% 100%,0 100%,0 30%);
    display:flex;align-items:center;padding-left:85px}
  .headline{color:#fff;font-size:37px;font-weight:400;line-height:1.5;text-transform:uppercase;letter-spacing:.5px}

  .features{left:0;top:1000px;width:1040px;height:295px}
  .features-row{position:absolute;left:0;width:1040px;height:148px;display:flex;padding:0 40px 0 53px;gap:30px;align-items:center}
  .features-row--dark{top:0;background:var(--ink)}
  .features-row--light{top:148px;background:#fff}
  .feature{flex:1;display:flex;gap:14px;align-items:flex-start}
  .feature-icon{flex:0 0 40px;width:40px;height:40px;background:var(--orange);border-radius:4px;display:flex;align-items:center;justify-content:center}
  .feature-text{font-size:16px;line-height:1.4}
  .features-row--dark .feature-text{color:#eaeaea}
  .features-row--light .feature-text{color:var(--text-dark)}

  .contact-strip{left:0;top:1295px;width:1040px;height:97px;background:var(--ink-soft);display:flex;align-items:center;padding:0 53px;justify-content:space-between}
  .cta-line{color:var(--orange);font-style:italic;font-size:16px;line-height:1.45;width:520px}
  .contact-list{list-style:none;color:#e6e6e6;font-size:14px;line-height:1.75;width:380px}
  .contact-list li{display:flex;align-items:center;gap:10px}
  .dot-icon{width:14px;height:14px;border-radius:50%;background:var(--orange);flex:0 0 14px}

  .footer{left:0;top:1392px;width:1040px;height:79px;background:#fff;display:flex;align-items:center;padding:0 53px;justify-content:space-between}
  .partner-badges{display:flex;gap:40px;align-items:center}
  .badge{width:170px;height:42px;border-radius:6px;background:#e4e4e4}
  .badge--round{width:150px;border-radius:21px;background:#dcdcdc}
  .phone-line{display:flex;align-items:center;gap:14px;color:var(--ink);font-size:38px;font-weight:600}

  /* ---------- back ---------- */
  .intro-band{left:0;top:26px;width:1040px;height:150px;background:var(--orange);display:flex;align-items:center;padding:0 53px}
  .intro-text{color:#fff;font-size:32px;line-height:1.3;font-weight:600;width:860px}
  .photo-hand{left:0;top:212px;width:530px;height:360px;border-top-right-radius:40px;
    background:linear-gradient(135deg,#c9b49b 0%,#8a6e52 45%,#3a3230 100%)}
  .photo-kitchen{left:548px;top:212px;width:492px;height:380px;
    clip-path:polygon(12% 0,100% 0,100% 100%,0 100%);
    background:linear-gradient(160deg,#f4f2ef 0%,#d7d3cd 55%,#9c958c 100%)}
  .benefits{left:0;top:534px;width:1040px;height:456px;background:var(--ink);
    clip-path:polygon(0 8%,50% 8%,53% 0,100% 0,100% 100%,0 100%)}
  .benefits-glow{left:380px;top:600px;width:280px;height:300px;border-radius:50%;
    background:radial-gradient(circle,rgba(255,255,255,.12) 0%,rgba(255,255,255,0) 70%)}
  .benefits-title{left:80px;top:600px;color:var(--orange);font-size:24px;font-weight:600;text-transform:uppercase}
  .benefit-list{list-style:none;position:absolute;top:660px;display:flex;flex-direction:column;gap:30px}
  .benefit-list--left{left:80px;width:370px}
  .benefit-list--right{left:560px;width:440px}
  .benefit{display:flex;gap:22px;align-items:center;color:#e6e6e6;font-size:16px;line-height:1.4;min-height:44px}
  .hex{flex:0 0 40px;width:40px;height:44px;background:var(--orange);
    clip-path:polygon(50% 0,100% 25%,100% 75%,50% 100%,0 75%,0 25%)}
  .frame-lines{left:0;top:950px;width:1040px;height:521px}
  .illustration-home{left:0;top:1000px;width:555px;height:390px;
    background:linear-gradient(150deg,#f3f3f3 0%,#d9dcd6 50%,#9fb57e 100%)}
  .brand-box--back{left:88px;top:1281px;width:205px;height:190px;gap:10px}
  .brand-box--back .brand-square{width:14px;height:14px;flex-basis:14px}
  .brand-box--back .brand-name{font-size:20px}
  .about-text{left:574px;top:1030px;width:440px;color:var(--text-dark);font-size:16.5px;line-height:1.45;text-align:justify}
  .promise{left:574px;top:1262px;width:440px;color:var(--orange);font-size:22px;line-height:1.3}
  .phone-line--back{left:574px;top:1392px;font-size:30px}
</style>
</head>
<body>

<!-- FRONT PAGE -->
<section class="page page--front">
  <div class="photo hero-photo" role="img" aria-label="Photograph of a CCTV camera in a bright room with two smartphones showing the security app"></div>
  <svg class="abs hero-decor" viewBox="0 0 1040 1000" aria-hidden="true">
    <rect x="334" y="322" width="706" height="22" fill="var(--orange)"/>
    <polygon points="890,560 1040,380 1040,470 950,580" fill="var(--orange)"/>
    <polygon points="540,846 1040,846 1040,1000 430,1000" fill="var(--ink)"/>
  </svg>

  <div class="abs brand-box brand-box--front">
    <span class="brand-square"></span>
    <span class="brand-name">R T Security</span>
  </div>

  <div class="abs headline-box">
    <h1 class="headline">Are you looking to<br>keep you or your<br>premises safe?</h1>
  </div>

  <div class="abs features">
    <div class="features-row features-row--dark">
      <div class="feature">
        <span class="feature-icon"><svg width="22" height="22" viewBox="0 0 22 22"><path d="M3 11l5 5 11-11" stroke="#fff" stroke-width="3" fill="none"/></svg></span>
        <p class="feature-text">We install, maintain and repair all intruder alarms, CCTV, intercom and access control</p>
      </div>
      <div class="feature">
        <span class="feature-icon"><svg width="22" height="22" viewBox="0 0 22 22"><circle cx="11" cy="11" r="7" stroke="#fff" stroke-width="3" fill="none"/></svg></span>
        <p class="feature-text">View, control and manage your security systems anywhere in the world with smartphone apps</p>
      </div>
      <div class="feature">
        <span class="feature-icon"><svg width="22" height="22" viewBox="0 0 22 22"><rect x="4" y="4" width="14" height="14" stroke="#fff" stroke-width="3" fill="none"/></svg></span>
        <p class="feature-text">Feel at ease with monitoring services and police response tailored to suit you and your business</p>
      </div>
    </div>
    <div class="features-row features-row--light">
      <div class="feature">
        <span class="feature-icon"><svg width="22" height="22" viewBox="0 0 22 22"><path d="M3 11l5 5 11-11" stroke="#fff" stroke-width="3" fill="none"/></svg></span>
        <p class="feature-text">We can takeover any existing security system and offer maintenance checks to guarantee the best performance for you and your premises</p>
      </div>
      <div class="feature">
        <span class="feature-icon"><svg width="22" height="22" viewBox="0 0 22 22"><path d="M11 3l8 7v9H3v-9z" fill="#fff"/></svg></span>
        <p class="feature-text">We understand that being security conscious is ever increasing, protecting your property and family is a number one priority</p>
      </div>
      <div class="feature">
        <span class="feature-icon"><svg width="22" height="22" viewBox="0 0 22 22"><path d="M11 2l8 3v6c0 5-4 8-8 9-4-1-8-4-8-9V5z" fill="#fff"/></svg></span>
        <p class="feature-text">Our fully insured and accredited team offer quality, safety and cost efficiency throughout and whole process</p>
      </div>
    </div>
  </div>

  <div class="abs contact-strip">
    <p class="cta-line">If you are looking to improve the security in your home, office or commercial property then call a member of our team today for a free quote.</p>
    <ul class="contact-list">
      <li><span class="dot-icon"></span>operations@rtsecuritysystems.co.uk</li>
      <li><span class="dot-icon"></span>www.rtsecuritysystems.co.uk</li>
      <li><span class="dot-icon"></span>14 Harlow Lane, Oakfield, Essex, CM99 1AB</li>
    </ul>
  </div>

  <div class="abs footer">
    <div class="partner-badges">
      <span class="badge badge--round"></span>
      <span class="badge"></span>
    </div>
    <div class="phone-line">
      <svg width="30" height="30" viewBox="0 0 24 24"><path d="M6.6 10.8a15.1 15.1 0 006.6 6.6l2.2-2.2c.3-.3.7-.4 1-.2 1.1.4 2.3.6 3.6.6.6 0 1 .4 1 1V20c0 .6-.4 1-1 1A17 17 0 013 4c0-.6.4-1 1-1h3.5c.6 0 1 .4 1 1 0 1.3.2 2.5.6 3.6.1.3 0 .7-.2 1z" fill="var(--orange)"/></svg>
      <span>01632 960418</span>
    </div>
  </div>
</section>

<!-- BACK PAGE -->
<section class="page page--back">
  <div class="abs intro-band">
    <h2 class="intro-text">R T Security Systems are using the latest cloud-based technology to stay connected with your home and business 24/7.</h2>
  </div>

  <div class="photo photo-hand" role="img" aria-label="Photograph of a hand holding a smartphone running the security app beside a coffee cup"></div>
  <div class="photo photo-kitchen" role="img" aria-label="Photograph of a wall-mounted alarm touch panel in a modern kitchen"></div>

  <div class="abs benefits"></div>
  <div class="abs benefits-glow" aria-hidden="true"></div>
  <h3 class="abs benefits-title">Some benefits of cloud services are;</h3>
  <ul class="benefit-list benefit-list--left">
    <li class="benefit"><span class="hex"></span>High level support 24/7</li>
    <li class="benefit"><span class="hex"></span>Reduce engineer call outs and running costs</li>
    <li class="benefit"><span class="hex"></span>Identify issues in advance</li>
    <li class="benefit"><span class="hex"></span>Remotely manage systems to ensure correct operation</li>
  </ul>
  <ul class="benefit-list benefit-list--right">
    <li class="benefit"><span class="hex"></span>Remote health checks carried out to keep your system performing as it should</li>
    <li class="benefit"><span class="hex"></span>Automatically update your system with the latest releases via cloud application software</li>
    <li class="benefit"><span class="hex"></span>Interact, control and integrate your security system like never before</li>
  </ul>

  <div class="photo illustration-home" role="img" aria-label="Illustration of a cut-away home fitted with alarm sensors and detectors"></div>
  <svg class="abs frame-lines" viewBox="0 0 1040 521" aria-hidden="true">
    <polygon points="555,40 1040,40 1040,52 567,52 555,70" fill="var(--orange)"/>
  </svg>

  <div class="abs brand-box brand-box--back">
    <span class="brand-square"></span>
    <span class="brand-name">R T Security</span>
  </div>

  <p class="abs about-text">With the new cloud-based system we can check the alarm performance anytime you need it. This gives us the capability to assist you in any of your needs, be that changing user codes or system configuration. We are always there, working in the background to make sure you have the support and help you need. This is taking alarm systems into the future and leaving the stand-alone systems in the past.</p>
  <p class="abs promise">R T Security Systems are always there, always available, wherever and whenever you need us.</p>
  <div class="abs phone-line phone-line--back">
    <svg width="26" height="26" viewBox="0 0 24 24"><path d="M6.6 10.8a15.1 15.1 0 006.6 6.6l2.2-2.2c.3-.3.7-.4 1-.2 1.1.4 2.3.6 3.6.6.6 0 1 .4 1 1V20c0 .6-.4 1-1 1A17 17 0 013 4c0-.6.4-1 1-1h3.5c.6 0 1 .4 1 1 0 1.3.2 2.5.6 3.6.1.3 0 .7-.2 1z" fill="var(--orange)"/></svg>
    <span>01632 960418</span>
  </div>
</section>

</body>
</html>
```